New Business and Accounting Software need a Web Site

The website is for a Business and Accounting Software that has 8 products.
Each product has its owns logo and color, when you do the design have in consideration that we are looking the experience that when you change from one product page to another the look and feel adjust to the color and logo of the product.
The product are:
Ventas (Sales)
Compras (Purchases)
Contabilidad (Accounting)
Presupuesto (Budget)
Inventarios (Inventory)
Bancos (Banks)
NĂ³mina RH (Human Resources Payroll)
CRM (Customer Relationship Manager)

You can see how the main logo and variations are used in each page
- https://www.vemu.com/
- https://www.lari.com/
- https://www.tovimal.com/

Our goal is to be similar to them.

I have created a word document to explain what I want.
You need to design:
1 Home Page
1 Product Landing Page
1 Product Detail Page
1 Price Page

I am attaching:
1. Main Logo
2. 8 Product Logos
3. Website Idea, you can create your own idea.

You are welcome to use other icons for the each product if you want.

Independet professionals and Small and Medium Companies

Business and Accounting Software

Coded - Design and coding required

0054AA
0677BA
7BADD7
CADEEF
E8F1F8

• Must show all products in the main page

```html
<!DOCTYPE html>
<html lang="en">
<head>
<meta charset="utf-8">
<title>Ledgra — Business and Accounting Software</title>
<link rel="stylesheet" href="https://fonts.googleapis.com/css2?family=Poppins:ital,wght@0,400;0,500;0,600;0,700;1,400&display=swap">
<style>
:root{
  --blue-deep:#0054aa;
  --blue:#0677ba;
  --blue-soft:#7badd7;
  --blue-pale:#cadeef;
  --blue-mist:#e8f1f8;
  --ink:#1c1c1c;
  --text:#3a3a3a;
  --muted:#7a7a7a;
  --footer:#1f2327;
  --ventas:#d9793a;
  --compras:#7ba3c4;
  --contabilidad:#c2549e;
  --presupuesto:#2fa876;
  --inventarios:#9b3a43;
  --bancos:#5a5a5a;
  --nomina:#5bb38a;
  --crm:#5c5fc9;
}
*{box-sizing:border-box;margin:0;padding:0}
html,body{width:1200px;height:5319px;overflow:hidden}
body{font-family:"Poppins",sans-serif;color:var(--text);background:#fff;position:relative}
a{color:inherit;text-decoration:none}

/* Brand */
.brand{display:flex;align-items:center;gap:10px}
.brand__mark{width:58px;height:58px;border-radius:50%;background:var(--blue-deep)}
.brand__name{font-weight:600;font-size:44px;color:var(--blue-deep);line-height:1}

/* Header */
.site-header{position:absolute;top:0;left:0;width:1200px;height:96px}
.site-header .brand{position:absolute;left:142px;top:18px}
.nav{position:absolute;left:414px;top:36px;display:flex;gap:32px;font-size:14px;font-weight:500;color:var(--ink)}
.nav__item--active{color:var(--blue-deep)}
.auth{position:absolute;left:836px;top:28px;display:flex;gap:14px}
.pill{display:inline-flex;align-items:center;justify-content:center;border-radius:22px;font-size:11px;font-weight:700;text-transform:uppercase;color:#fff;letter-spacing:.3px}
.auth .pill{width:106px;height:40px}
.pill--dark{background:var(--blue-deep)}
.pill--soft{background:var(--blue-soft)}

/* Hero */
.hero{position:absolute;top:96px;left:0;width:1200px;height:560px}
.hero__halo{position:absolute;left:-10px;top:-14px;width:400px;height:400px;border-radius:50%;background:#f1f6fb}
.hero__title{position:absolute;left:142px;top:66px;font-size:50px;line-height:54px;font-weight:700;color:var(--blue-deep)}
.hero__lead{position:absolute;left:142px;top:252px;width:380px;font-size:13.5px;line-height:24px;font-weight:600;color:var(--ink)}
.hero__cta{position:absolute;left:142px;top:358px;width:147px;height:38px;background:var(--blue-deep)}
.hero__visual{position:absolute;left:560px;top:20px;width:630px;height:470px;border-radius:50% 40% 45% 50%;background:radial-gradient(circle at 55% 45%,#cfe0ef 0,#7badd7 45%,#0054aa 100%)}
.hero__dots{position:absolute;left:142px;top:462px;display:flex;gap:22px}
.hero__dots span{width:10px;height:10px;border-radius:50%;background:#c8ccd2}
.hero__dots .is-on{background:var(--blue)}
.hero__down{position:absolute;left:436px;top:480px;width:44px;height:44px;border:2px solid var(--ink);border-radius:50%;display:flex;align-items:center;justify-content:center}

/* Section headings */
.section-title{position:absolute;left:0;width:1200px;text-align:center;font-size:36px;font-weight:700;color:var(--ink)}
.section-title::after{content:"";display:block;width:34px;height:4px;background:var(--blue-deep);margin:10px auto 0}

/* Products */
.product{position:absolute;left:0;width:1200px;height:403px}
.product__glow{position:absolute;width:180px;height:180px;border-radius:50%;background:radial-gradient(circle at 60% 40%,var(--accent),var(--blue-deep))}
.product__screen{position:absolute;width:420px;height:200px;border-radius:6px;background:linear-gradient(180deg,var(--blue-deep) 0 6px,#fbfcfe 6px,#eef1f5 100%);box-shadow:0 12px 30px rgba(0,0,0,.14)}
.product--left .product__glow{left:83px;top:166px}
.product--left .product__screen{left:171px;top:58px}
.product--left .product__info{left:650px}
.product--right .product__glow{left:932px;top:136px}
.product--right .product__screen{left:609px;top:52px}
.product--right .product__info{left:173px}
.product__info{position:absolute;top:18px;width:376px}
.product-logo{display:flex;align-items:center;gap:8px}
.product-logo__mark{width:62px;height:62px;border-radius:50%;background:var(--accent)}
.product-logo__name{font-size:44px;font-weight:600;color:var(--blue-deep);line-height:1}
.product-logo__sub{display:block;font-size:12px;letter-spacing:5px;color:var(--accent);text-transform:uppercase;font-weight:500;margin-top:2px}
.product__text{margin-top:18px;font-size:13px;line-height:24px;text-align:justify;color:var(--text)}
.product__cta{margin-top:20px;width:148px;height:38px;background:var(--accent)}

/* Reviews */
.reviews{position:absolute;left:0;top:4027px;width:1200px;height:558px;background:linear-gradient(180deg,#e4eef8,#edf3f9)}
.reviews .section-title{top:100px}
.review{position:absolute;top:196px;width:368px;height:186px;background:#fff;padding:26px 28px}
.review--featured{box-shadow:0 10px 28px rgba(0,0,0,.16);top:190px}
.review__quote{font-style:italic;font-size:13px;line-height:24px;color:var(--text);text-align:justify}
.review__meta{display:flex;align-items:center;margin-top:14px;gap:10px}
.review__name{font-size:11px;font-weight:700;color:var(--blue-deep)}
.review__stars{color:#e8a21a;font-size:13px;letter-spacing:1px}
.review__source{margin-left:auto;display:flex;align-items:center;gap:5px;font-size:18px;font-weight:600;color:var(--ink)}
.review__source i{width:16px;height:16px;border-radius:50%;background:var(--ink)}
.reviews__arrow{position:absolute;top:270px}
.reviews__more{position:absolute;left:499px;top:419px;width:202px;height:40px;background:var(--blue-deep)}

/* Contact */
.contact{position:absolute;left:0;top:4600px;width:1200px;height:630px}
.contact .section-title{top:80px}
.contact__info{position:absolute;left:155px;top:197px;width:456px;height:345px;background:var(--blue-mist);padding:40px 0 0 60px}
.info-row{display:flex;align-items:center;gap:30px;height:100px}
.info-row__icon{width:66px;height:66px;border-radius:50%;background:var(--blue-deep);display:flex;align-items:center;justify-content:center;flex:none}
.info-row__label{font-size:12px;font-weight:700;color:var(--ink);text-transform:uppercase}
.info-row__value{font-size:17px;line-height:22px;color:var(--ink);margin-top:4px}
.info-row__value--phone{color:var(--blue-deep);font-weight:700;letter-spacing:1px}
.contact__form{position:absolute;left:644px;top:200px;width:402px}
.field{display:block;width:100%;height:41px;border:1px solid #c8ccd2;margin-bottom:11px;padding:12px 22px;font-size:11px;color:var(--ink);text-transform:uppercase}
.field--message{height:120px}
.contact__submit{margin-top:16px;width:402px;height:56px;background:var(--blue-deep);font-size:20px;border-radius:30px}

/* Footer */
.site-footer{position:absolute;left:0;top:5239px;width:1200px;height:80px;background:var(--footer)}
.site-footer .brand{position:absolute;left:142px;top:13px}
.site-footer .brand__mark{width:52px;height:52px;background:var(--blue)}
.site-footer .brand__name{font-size:38px;color:var(--blue-soft)}
.site-footer__legal{position:absolute;left:412px;top:32px;font-size:10px;color:#e6e6e6}
.social{position:absolute;left:962px;top:28px;display:flex;gap:8px}
.social span{width:24px;height:24px;border-radius:50%;background:var(--blue)}
.social span:last-child{background:transparent;border:2px solid var(--blue)}
</style>
</head>
<body>

<header class="site-header">
  <a class="brand" href="#"><span class="brand__mark"></span><span class="brand__name">Ledgra</span></a>
  <nav class="nav">
    <a class="nav__item nav__item--active" href="#">Home</a>
    <a class="nav__item" href="#">Products</a>
    <a class="nav__item" href="#">Pricing</a>
    <a class="nav__item" href="#">About</a>
    <a class="nav__item" href="#">Contact</a>
  </nav>
  <div class="auth">
    <a class="pill pill--dark" href="#">Sign in</a>
    <a class="pill pill--soft" href="#">Sign up</a>
  </div>
</header>

<section class="hero">
  <span class="hero__halo" aria-hidden="true"></span>
  <h1 class="hero__title">Business and<br>Accounting<br>Software</h1>
  <p class="hero__lead">Lorem ipsum dolor sit amet, consectetur adipiscing elit, sed do eiusmod tempor incididunt ut labore et dolore magnais ipsum suspendisse ultrices</p>
  <a class="pill hero__cta" href="#">Get started</a>
  <div class="hero__visual" role="img" aria-label="Desktop monitor showing the accounting dashboard with a chart"></div>
  <div class="hero__dots"><span></span><span class="is-on"></span><span></span><span></span></div>
  <a class="hero__down" href="#products" aria-label="Scroll down">
    <svg width="20" height="20" viewBox="0 0 20 20" fill="none" stroke="#1c1c1c" stroke-width="2"><path d="M4 5l6 5 6-5M4 10l6 5 6-5"/></svg>
  </a>
</section>

<h2 class="section-title" id="products" style="top:712px">Featured Products</h2>

<section class="product product--left" style="top:805px;--accent:var(--ventas)">
  <span class="product__glow" aria-hidden="true"></span>
  <div class="product__screen" role="img" aria-label="Sales module screen with order list"></div>
  <div class="product__info">
    <div class="product-logo"><span class="product-logo__mark"></span><div><span class="product-logo__name">Ledgra</span><span class="product-logo__sub">Ventas</span></div></div>
    <p class="product__text">Lorem ipsum dolor sit amet, consectetur adipiscing elit, sed do eiusmod tempor incididunt ut labore et dolore magnais ipsum suspendisse ulorem ipsum dolor sit amet, consectetur adipiscing elit, sed do eiusmod tempor incididunt ut labore et dolore magnais</p>
    <a class="pill product__cta" href="#">Get started</a>
  </div>
</section>

<section class="product product--right" style="top:1208px;--accent:var(--compras)">
  <span class="product__glow" aria-hidden="true"></span>
  <div class="product__screen" role="img" aria-label="Purchases module screen with supplier list"></div>
  <div class="product__info">
    <div class="product-logo"><span class="product-logo__mark"></span><div><span class="product-logo__name">Ledgra</span><span class="product-logo__sub">Compras</span></div></div>
    <p class="product__text">Lorem ipsum dolor sit amet, consectetur adipiscing elit, sed do eiusmod tempor incididunt ut labore et dolore magnais ipsum suspendisse ulorem ipsum dolor sit amet, consectetur adipiscing elit, sed do eiusmod tempor incididunt ut labore et dolore magnais</p>
    <a class="pill product__cta" href="#">Get started</a>
  </div>
</section>

<section class="product product--left" style="top:1611px;--accent:var(--contabilidad)">
  <span class="product__glow" aria-hidden="true"></span>
  <div class="product__screen" role="img" aria-label="Accounting module screen with ledger entries"></div>
  <div class="product__info">
    <div class="product-logo"><span class="product-logo__mark"></span><div><span class="product-logo__name">Ledgra</span><span class="product-logo__sub">Contabilidad</span></div></div>
    <p class="product__text">Lorem ipsum dolor sit amet, consectetur adipiscing elit, sed do eiusmod tempor incididunt ut labore et dolore magnais ipsum suspendisse ulorem ipsum dolor sit amet, consectetur adipiscing elit, sed do eiusmod tempor incididunt ut labore et dolore magnais</p>
    <a class="pill product__cta" href="#">Get started</a>
  </div>
</section>

<section class="product product--right" style="top:2013px;--accent:var(--presupuesto)">
  <span class="product__glow" aria-hidden="true"></span>
  <div class="product__screen" role="img" aria-label="Budget module screen with budget lines"></div>
  <div class="product__info">
    <div class="product-logo"><span class="product-logo__mark"></span><div><span class="product-logo__name">Ledgra</span><span class="product-logo__sub">Presupuesto</span></div></div>
    <p class="product__text">Lorem ipsum dolor sit amet, consectetur adipiscing elit, sed do eiusmod tempor incididunt ut labore et dolore magnais ipsum suspendisse ulorem ipsum dolor sit amet, consectetur adipiscing elit, sed do eiusmod tempor incididunt ut labore et dolore magnais</p>
    <a class="pill product__cta" href="#">Get started</a>
  </div>
</section>

<section class="product product--left" style="top:2416px;--accent:var(--inventarios)">
  <span class="product__glow" aria-hidden="true"></span>
  <div class="product__screen" role="img" aria-label="Inventory module screen with stock items"></div>
  <div class="product__info">
    <div class="product-logo"><span class="product-logo__mark"></span><div><span class="product-logo__name">Ledgra</span><span class="product-logo__sub">Inventarios</span></div></div>
    <p class="product__text">Lorem ipsum dolor sit amet, consectetur adipiscing elit, sed do eiusmod tempor incididunt ut labore et dolore magnais ipsum suspendisse ulorem ipsum dolor sit amet, consectetur adipiscing elit, sed do eiusmod tempor incididunt ut labore et dolore magnais</p>
    <a class="pill product__cta" href="#">Get started</a>
  </div>
</section>

<section class="product product--right" style="top:2819px;--accent:var(--bancos)">
  <span class="product__glow" aria-hidden="true"></span>
  <div class="product__screen" role="img" aria-label="Banks module screen with account movements"></div>
  <div class="product__info">
    <div class="product-logo"><span class="product-logo__mark"></span><div><span class="product-logo__name">Ledgra</span><span class="product-logo__sub">Bancos</span></div></div>
    <p class="product__text">Lorem ipsum dolor sit amet, consectetur adipiscing elit, sed do eiusmod tempor incididunt ut labore et dolore magnais ipsum suspendisse ulorem ipsum dolor sit amet, consectetur adipiscing elit, sed do eiusmod tempor incididunt ut labore et dolore magnais</p>
    <a class="pill product__cta" href="#">Get started</a>
  </div>
</section>

<section class="product product--left" style="top:3221px;--accent:var(--nomina)">
  <span class="product__glow" aria-hidden="true"></span>
  <div class="product__screen" role="img" aria-label="Payroll module screen with employee payments"></div>
  <div class="product__info">
    <div class="product-logo"><span class="product-logo__mark"></span><div><span class="product-logo__name">Ledgra</span><span class="product-logo__sub">Nómina RH</span></div></div>
    <p class="product__text">Lorem ipsum dolor sit amet, consectetur adipiscing elit, sed do eiusmod tempor incididunt ut labore et dolore magnais ipsum suspendisse ulorem ipsum dolor sit amet, consectetur adipiscing elit, sed do eiusmod tempor incididunt ut labore et dolore magnais</p>
    <a class="pill product__cta" href="#">Get started</a>
  </div>
</section>

<section class="product product--right" style="top:3624px;--accent:var(--crm)">
  <span class="product__glow" aria-hidden="true"></span>
  <div class="product__screen" role="img" aria-label="CRM module screen with contact cards"></div>
  <div class="product__info">
    <div class="product-logo"><span class="product-logo__mark"></span><div><span class="product-logo__name">Ledgra</span><span class="product-logo__sub">CRM</span></div></div>
    <p class="product__text">Lorem ipsum dolor sit amet, consectetur adipiscing elit, sed do eiusmod tempor incididunt ut labore et dolore magnais ipsum suspendisse ulorem ipsum dolor sit amet, consectetur adipiscing elit, sed do eiusmod tempor incididunt ut labore et dolore magnais</p>
    <a class="pill product__cta" href="#">Get started</a>
  </div>
</section>

<section class="reviews">
  <h2 class="section-title">Customer Reviews</h2>
  <svg class="reviews__arrow" style="left:12px" width="40" height="24" viewBox="0 0 40 24" fill="none" stroke="#a9b3bd" stroke-width="2"><path d="M38 12H3M13 2L3 12l10 10"/></svg>
  <svg class="reviews__arrow" style="left:1148px" width="40" height="24" viewBox="0 0 40 24" fill="none" stroke="#a9b3bd" stroke-width="2"><path d="M2 12h35M27 2l10 10-10 10"/></svg>
  <article class="review" style="left:31px">
    <p class="review__quote">Lorem ipsum dolor sit amet, consectetur adipiscing elit, sed do eiusmod tempor incididunt ut labore et dolore magna aliqua. Quis ipsum suspendisse ultrices gravida.</p>
    <div class="review__meta"><span class="review__name">MARA QUELL</span><span class="review__stars">★★★★★</span><span class="review__source"><i></i>Ostra</span></div>
  </article>
  <article class="review review--featured" style="left:417px">
    <p class="review__quote">Lorem ipsum dolor sit amet, consectetur adipiscing elit, sed do eiusmod tempor incididunt ut labore et dolore magna aliqua. Quis ipsum suspendisse ultrices gravida.</p>
    <div class="review__meta"><span class="review__name">MARA QUELL</span><span class="review__stars">★★★★★</span><span class="review__source"><i></i>Ostra</span></div>
  </article>
  <article class="review" style="left:801px">
    <p class="review__quote">Lorem ipsum dolor sit amet, consectetur adipiscing elit, sed do eiusmod tempor incididunt ut labore et dolore magna aliqua. Quis ipsum suspendisse ultrices gravida.</p>
    <div class="review__meta"><span class="review__name">MARA QUELL</span><span class="review__stars">★★★★★</span><span class="review__source"><i></i>Ostra</span></div>
  </article>
  <a class="pill reviews__more" href="#">View more reviews</a>
</section>

<section class="contact">
  <h2 class="section-title">Contact Us</h2>
  <div class="contact__info">
    <div class="info-row">
      <span class="info-row__icon"><svg width="24" height="30" viewBox="0 0 24 30"><path d="M12 0C5.4 0 0 5.2 0 11.7 0 20 12 30 12 30s12-10 12-18.3C24 5.2 18.6 0 12 0z" fill="#fff"/><circle cx="12" cy="11.5" r="4.5" fill="#0054aa"/></svg></span>
      <div><div class="info-row__label">Address</div><div class="info-row__value">2750 Harbor Lane<br>Alder Bay, CA 90412</div></div>
    </div>
    <div class="info-row">
      <span class="info-row__icon"><svg width="26" height="26" viewBox="0 0 24 24"><path fill="#fff" d="M6.6 10.8a15.2 15.2 0 006.6 6.6l2.2-2.2c.3-.3.7-.4 1-.2 1.1.4 2.3.6 3.6.6.6 0 1 .4 1 1V20c0 .6-.4 1-1 1A17 17 0 013 4c0-.6.4-1 1-1h3.5c.6 0 1 .4 1 1 0 1.3.2 2.5.6 3.6.1.3 0 .7-.2 1L6.6 10.8z"/></svg></span>
      <div><div class="info-row__label">Call us now</div><div class="info-row__value info-row__value--phone">555.010.2040</div></div>
    </div>
    <div class="info-row">
      <span class="info-row__icon"><svg width="26" height="20" viewBox="0 0 26 20"><rect width="26" height="20" rx="2" fill="#fff"/><path d="M1 2l12 9 12-9" fill="none" stroke="#0054aa" stroke-width="2"/></svg></span>
      <div><div class="info-row__label">E mail us</div><div class="info-row__value">info@ledgra.com</div></div>
    </div>
  </div>
  <form class="contact__form">
    <span class="field">Name</span>
    <span class="field">E mail</span>
    <span class="field">Phone</span>
    <span class="field field--message">Message</span>
    <span class="pill contact__submit">Submit</span>
  </form>
</section>

<footer class="site-footer">
  <a class="brand" href="#"><span class="brand__mark"></span><span class="brand__name">Ledgra</span></a>
  <p class="site-footer__legal">Copyrights @ 2022 Ledgra.All Rights Reserved &nbsp;|&nbsp; Privacy &nbsp;|&nbsp; Terms of Use</p>
  <div class="social" aria-label="Social links"><span></span><span></span><span></span></div>
</footer>

</body>
</html>
```